Photographer website, needs Facebook design. (updated details in brief.)

Company name Pell Voskin Photography, looking to add a Facebook design, that is minimalistic, yet powerful. Less is more in my opinion, but what's there is creative, but eye catchy. see example image in files section for a better idea of what I am looking for. I have also added some source files for my logo.

Target Market(s)

local musicians/artists, models/fashion, and business professional looking for headshots or corporate business profile images.

Colors
0655a3
cfdfed
ffffff

Requirements
Must have
• I have added a screen shot of what I am looking for, for everyone to gain a better sense of my vision. Please see the uploaded files below.
Nice to have
• I am really a fan of the example image in the files section below. Something close to that I would be very happy with.
Should not have
• should not have my face on the cover.

```html
<!DOCTYPE html>
<html lang="en">
<head>
<meta charset="utf-8">
<title>Pell Voskin Photography – Facebook Cover</title>
<link rel="stylesheet" href="https://fonts.googleapis.com/css2?family=Josefin+Sans:wght@600&family=Nunito:wght@800&display=swap">
<style>
  :root {
    --page-bg: #f2f2f2;
    --navy-deep: #04203a;
    --navy-mid: #0b3556;
    --navy-glow: #12456b;
    --charcoal: #181818;
    --white: #ffffff;
    --ink: #0d2540;
    --brand-blue: #0a4c80;
    --black: #050505;
    --silver-light: #e2e3e6;
    --silver-mid: #b9bbbf;
    --silver-dark: #8e9096;
    --tile-dark: #131a22;
    --tile-blue: #0e2f55;
    --tile-warm: #3a342c;
    --tile-sky: #59636a;
  }
  * { margin: 0; padding: 0; box-sizing: border-box; }
  html, body {
    width: 1200px; height: 1051px; overflow: hidden;
    background: var(--page-bg);
  }
  .cover {
    position: absolute; left: 46px; width: 1108px; height: 422px; overflow: hidden;
  }
  .cover--navy { top: 70px; }
  .cover--charcoal { top: 559px; background: var(--charcoal); }
  .cover__backdrop {
    position: absolute; inset: 0;
    background:
      radial-gradient(circle at 150px 210px, rgba(40,90,120,.35) 0, rgba(20,60,95,.2) 120px, transparent 230px),
      radial-gradient(ellipse at 620px 200px, var(--navy-glow) 0, transparent 360px),
      linear-gradient(135deg, var(--navy-mid), var(--navy-deep));
  }
  .brand {
    position: absolute; left: 0; width: 660px; top: 112px;
    text-align: center; color: var(--white);
    font-family: "Josefin Sans", sans-serif; font-weight: 600;
  }
  .brand__name { font-size: 44px; letter-spacing: 13px; line-height: 1; padding-left: 13px; }
  .brand__tag { font-size: 24px; letter-spacing: 8.5px; line-height: 1; margin-top: 12px; padding-left: 8px; }
  .url-pill {
    position: absolute; left: 118px; top: 241px; width: 410px; height: 61px;
    background: var(--white); border-radius: 31px;
  }
  .url-pill__text {
    position: absolute; left: 40px; top: 0; line-height: 61px;
    font-family: "Nunito", sans-serif; font-weight: 800; font-size: 28px; color: var(--ink);
  }
  .url-pill__button {
    position: absolute; left: 352px; top: 0; width: 61px; height: 61px;
  }
  .monitor { position: absolute; left: 661px; top: 65px; }
</style>
</head>
<body>

<svg width="0" height="0" style="position:absolute" aria-hidden="true">
  <defs>
    <linearGradient id="chin" x1="0" y1="0" x2="0" y2="1">
      <stop offset="0" stop-color="#d6d7da"/><stop offset="1" stop-color="#bfc1c5"/>
    </linearGradient>
    <linearGradient id="neck" x1="0" y1="0" x2="1" y2="0">
      <stop offset="0" stop-color="#9a9ca1"/><stop offset=".5" stop-color="#f1f1f2"/><stop offset="1" stop-color="#a4a6ab"/>
    </linearGradient>
    <symbol id="desktop-display" viewBox="0 0 366 320">
      <rect x="0" y="0" width="366" height="222" rx="7" fill="var(--black)"/>
      <rect x="15" y="15" width="336" height="189" fill="var(--white)"/>
      <g role="img" aria-label="Portfolio photo grid of portraits">
        <rect x="19" y="19" width="75" height="113" fill="var(--tile-warm)"/>
        <rect x="97" y="19" width="75" height="113" fill="var(--tile-dark)"/>
        <rect x="175" y="19" width="171" height="113" fill="var(--tile-blue)"/>
        <rect x="19" y="135" width="80" height="64" fill="var(--tile-dark)"/>
        <rect x="102" y="135" width="79" height="64" fill="var(--tile-dark)"/>
        <rect x="184" y="135" width="80" height="64" fill="var(--tile-sky)"/>
        <rect x="267" y="135" width="79" height="64" fill="var(--tile-warm)"/>
      </g>
      <path d="M0 218 H366 V250 a8 8 0 0 1 -8 8 H8 a8 8 0 0 1 -8 -8 Z" fill="url(#chin)"/>
      <path d="M145 258 H220 L224 298 H141 Z" fill="url(#neck)"/>
      <rect x="128" y="296" width="113" height="10" rx="4" fill="url(#neck)"/>
    </symbol>
  </defs>
</svg>

<section class="cover cover--navy">
  <div class="cover__backdrop" role="img" aria-label="Soft blue close-up of a camera lens"></div>
  <div class="brand">
    <h1 class="brand__name">PELL VOSKIN</h1>
    <p class="brand__tag">PHOTOGRAPHY</p>
  </div>
  <div class="url-pill">
    <span class="url-pill__text">www.pellvoskin.ca</span>
    <svg class="url-pill__button" viewBox="0 0 61 61" aria-hidden="true">
      <circle cx="30.5" cy="30.5" r="30.5" fill="var(--black)"/>
      <path d="M21 18 L45 30.5 L21 43 L26 30.5 Z" fill="var(--white)"/>
    </svg>
  </div>
  <svg class="monitor" width="366" height="320" aria-hidden="true"><use href="#desktop-display"/></svg>
</section>

<section class="cover cover--charcoal">
  <div class="brand">
    <h1 class="brand__name">PELL VOSKIN</h1>
    <p class="brand__tag">PHOTOGRAPHY</p>
  </div>
  <div class="url-pill">
    <span class="url-pill__text">www.pellvoskin.ca</span>
    <svg class="url-pill__button" viewBox="0 0 61 61" aria-hidden="true">
      <circle cx="30.5" cy="30.5" r="30.5" fill="var(--brand-blue)"/>
      <path d="M21 18 L45 30.5 L21 43 L26 30.5 Z" fill="var(--white)"/>
    </svg>
  </div>
  <svg class="monitor" width="366" height="320" aria-hidden="true"><use href="#desktop-display"/></svg>
</section>

</body>
</html>
```